Rebuild

Hello,
I got a new logo, and a new business name. Now I need that new identity on a new web page.
Please take a look at my existing site. www.critterfixhub.com
and please build me a new website with my new logo and get it posted at my new domain www.tomvarlowcapture.com
Updates
Please include in the design the Radio marketing tagline "Tom Varlow, Raised and Ready for Wildlife Control".
I would like to add that it is usually understood that I will capture and remove problem causing animals. However, what I really need to emphasize is that I fortify homes and other structures to keep the animals out long term. Trapping is a temporary solution. Home fortification such as reinforcing vent screens, sealing holes, and constructing secure barriers is the Permanent solution. Kind of like a home security system for vertebrate pests. You don't really need an alarm system if you have the best locks and steel doors.
Obviously, my website is a multiple page website. Some designs will be good for the home page, and others for secondary pages.
Ultimately, I need a good home page that will attract clients, and then good backup pages to explain the different aspects of my work.
I imagine a home page. Sub pages would include Home Fortifications, Species detail pages, Company history, FAQs, Odd and unusual services, specialties, and where to go for the things I don't do. The text for these pages is something I can write myself. I'm a good writer. Just not a very good visual artist.
I have added the logo in .eps, and I have also added the mirror image logo in both eps and jpg. Let me know if other formats are needed.
I've posted a bunch of photos on my facebook for perusal
http://www.facebook.com/pages/Tom-Varlow-Wildlife-Control/902315748160334
Target Market(s)
Upper to middle income homeowners
Industry/Entity Type
Business
Look and feel
Each slider illustrates characteristics of the customer's brand and the style your logo design should communicate.

```html
<!DOCTYPE html>
<html lang="en">
<head>
<meta charset="utf-8">
<title>Tom Varlow Wildlife Control</title>
<link href="https://fonts.googleapis.com/css2?family=Maven+Pro:wght@500;600;700&family=Arimo:wght@400;700&display=swap" rel="stylesheet">
<style>
:root{
  --ink:#1b1b1b;
  --orange:#f5a31a;
  --gold:#c98a12;
  --body-text:#7a7a7a;
  --light:#f1f1f1;
  --white:#ffffff;
}
*{margin:0;padding:0;box-sizing:border-box}
html,body{width:1043px;height:1200px;overflow:hidden}
body{position:relative;background:var(--light);font-family:"Arimo",Arial,sans-serif;color:var(--ink)}
.head{position:absolute;left:0;top:0;width:1043px;height:174px;background:var(--white);border-top:5px solid var(--ink)}
.brand{position:absolute;left:40px;top:62px;display:flex;align-items:center;gap:12px}
.brand-dot{width:36px;height:36px;border-radius:50%;background:var(--ink)}
.brand-name{font-family:"Maven Pro",sans-serif;font-weight:700;font-size:30px;color:var(--ink)}
.call{position:absolute;left:718px;top:0;width:289px;height:53px;background:linear-gradient(#4a4a4a,#1d1d1d);border-radius:0 0 14px 14px;text-align:center;font-family:"Maven Pro",sans-serif}
.call-label{color:#f2c200;font-weight:700;font-size:15px;padding-top:3px}
.call-phone{color:var(--white);font-weight:500;font-size:27px;line-height:28px}
.area{position:absolute;right:39px;top:62px;font-family:"Maven Pro",sans-serif;font-weight:500;font-size:26px;color:#a9a9a9}
.toplinks{position:absolute;right:14px;top:129px;font-family:"Maven Pro",sans-serif;font-weight:600;font-size:14px;color:#a9a9a9;display:flex;gap:22px}
.hero{position:absolute;left:11px;top:213px;width:1019px;height:298px;border-radius:8px;overflow:hidden;display:flex;box-shadow:0 4px 8px rgba(0,0,0,.25)}
.hero-panel{flex:1}
.p1{background:linear-gradient(135deg,#f0c98a,#b88955 55%,#4a4a3a)}
.p2{background:linear-gradient(160deg,#8c6b43,#c07a3a 50%,#6d4a26)}
.p3{background:linear-gradient(160deg,#d6c9aa,#2a2a2a 45%,#c9b890)}
.nav-ribbon{position:absolute;left:80px;top:196px;width:910px;height:54px}
.nav{position:absolute;left:117px;top:187px;width:837px;height:53px;background:linear-gradient(#ffc44a,var(--orange));border-radius:3px;display:flex;justify-content:center;align-items:center;box-shadow:0 3px 5px rgba(0,0,0,.3)}
.nav a{font-family:"Maven Pro",sans-serif;font-weight:700;font-size:15px;color:var(--ink);text-decoration:none;padding:0 11px;border-left:1px solid #d58a10;line-height:30px}
.nav a:first-child{border-left:none}
.intro{position:absolute;left:13px;top:545px;width:645px}
.intro h1{font-family:"Maven Pro",sans-serif;font-weight:600;font-size:20px;letter-spacing:.6px;margin-bottom:12px}
.intro p{font-size:12.3px;line-height:18.5px;color:var(--body-text);text-align:justify;margin-bottom:18px}
.intro .tagline{color:var(--ink)}
.intro .more{color:var(--ink)}
.quick{position:absolute;left:691px;top:544px;width:340px;height:272px;background:var(--white);border:2px solid #d6d6d6;border-radius:8px}
.quick h2{font-family:"Maven Pro",sans-serif;font-weight:600;font-size:19px;text-align:center;margin-top:18px}
.quick h2::before,.quick h2::after{content:"";display:inline-block;width:55px;height:1px;background:#999;vertical-align:middle;margin:0 10px}
.quick p{font-size:10.3px;line-height:18px;color:var(--gold);text-align:justify;margin:14px 12px 0}
.field{position:absolute;background:#dcdcdc;border:1px solid #c8c8c8;font-size:12px;color:#8a8a8a;padding:6px 8px}
.send{position:absolute;right:-2px;bottom:-2px;width:110px;height:33px;background:var(--ink);color:var(--white);font-family:"Maven Pro",sans-serif;font-weight:600;font-size:15px;text-align:center;line-height:33px;border-radius:4px 0 6px 0}
.tab{position:absolute;height:36px;background:linear-gradient(#3a3a3a,#141414);border-radius:6px;color:var(--white);font-family:"Maven Pro",sans-serif;font-weight:600;font-size:15px;line-height:36px;padding:0 12px}
.list{position:absolute;list-style:none;font-family:"Maven Pro",sans-serif;font-weight:600;font-size:15px;color:var(--gold)}
.list li{padding-left:19px;position:relative}
.list li::before{content:"";position:absolute;left:0;top:6px;border-left:6px solid var(--gold);border-top:4px solid transparent;border-bottom:4px solid transparent}
.services li{line-height:24px}
.reasons li{line-height:25.2px}
.social{position:absolute;left:906px;top:843px;width:126px;height:231px;background:linear-gradient(#1f1f1f,#3c3c3c);border-radius:6px;text-align:center;color:var(--white);font-family:"Maven Pro",sans-serif;font-weight:600;font-size:15px;line-height:22px;padding-top:10px}
.social-mark{width:79px;height:70px;margin:22px auto 0;background:var(--white);display:flex;align-items:center;justify-content:center;font-size:12px;color:var(--ink);font-weight:700}
.like{width:48px;height:24px;margin:20px auto 0;background:#eef1f6;border:1px solid #aab;border-radius:3px;font-size:11px;color:#333;line-height:22px;font-family:"Arimo",sans-serif}
.foot{position:absolute;left:0;top:1100px;width:1043px;height:100px;background:linear-gradient(#141414,#2e2e2e 85%,#e9e9e9 85%)}
.foot-links{position:absolute;left:12px;top:34px;display:flex;gap:12px;font-family:"Maven Pro",sans-serif;font-weight:600;font-size:12.5px;color:#d8d8d8}
.pay-label{position:absolute;right:12px;top:12px;font-family:"Maven Pro",sans-serif;font-weight:700;font-size:13px;color:var(--white)}
.pay{position:absolute;right:12px;top:36px;display:flex;gap:5px}
.pay span{width:42px;height:26px;border-radius:4px;background:linear-gradient(#f4f4f4,#bdbdbd);font-size:10px;font-weight:700;color:#333;text-align:center;line-height:26px}
.legal{position:absolute;left:0;top:72px;width:1043px;text-align:center;font-family:"Maven Pro",sans-serif;font-size:11.5px;font-weight:500;color:#5a5a5a}
</style>
</head>
<body>
<header class="head">
  <div class="brand"><span class="brand-dot"></span><span class="brand-name">Tom Varlow</span></div>
  <div class="call"><div class="call-label">CALL US NOW</div><div class="call-phone">360-555-0148</div></div>
  <div class="area">SERVING PUGET SOUND</div>
  <nav class="toplinks"><span>WHY CHOOSE US?</span><span>FIND US ON FRIENDBOOK</span></nav>
</header>

<div class="hero">
  <div class="hero-panel p1" role="img" aria-label="Photo of a man sitting with a dog at sunset"></div>
  <div class="hero-panel p2" role="img" aria-label="Photo of a puppy behind a chain-link fence"></div>
  <div class="hero-panel p3" role="img" aria-label="Photo of a black kitten on a wicker basket"></div>
</div>

<svg class="nav-ribbon" viewBox="0 0 910 54" aria-hidden="true">
  <polygon points="0,0 38,0 38,44 16,54 22,24" fill="#e9851a"/>
  <polygon points="910,0 872,0 872,44 894,54 888,24" fill="#e9851a"/>
</svg>
<nav class="nav">
  <a>HOME</a><a>ABOUT US</a><a>ANIMAL CONTROL</a><a>WILDLIFE SERVICES</a><a>TESTIMONIALS</a><a>CONTACT US</a>
</nav>

<section class="intro">
  <h1>ANIMAL PROBLEMS GONE. PERMANENT SOLUTIONS</h1>
  <p><span class="tagline">Tom Varlow, Raised and Ready for Wildlife Control.</span> If you have unwanted animals on your property in Thurston, Lewis, or Pierce Counties, I will capture and remove them. But trapping is only a temporary fix. The permanent solution is home fortification: reinforced vent screens, sealed holes and secure barriers that keep animals out long term.</p>
  <p>Think of it as a home security system for vertebrate pests. You don’t really need an alarm if you have the best locks and steel doors. I fortify homes and other structures for residential, commercial and industrial clients, so the job is done right the first time. I have extensive training, a lifelong passion for the wildlife of Western Washington, and I always solve the problem in the most gentle and humane way possible. <span class="more">Read More...</span></p>
</section>

<aside class="quick">
  <h2>QUICK CONTACT</h2>
  <p>PLEASE FILL THE FORM BELOW OR FOR IMMEDIATE RESPONSE CALL US TODAY! 360-555-0148.</p>
  <div class="field" style="left:12px;top:106px;width:155px;height:31px">Name</div>
  <div class="field" style="left:12px;top:142px;width:155px;height:31px">Email</div>
  <div class="field" style="left:12px;top:176px;width:155px;height:31px">Phone</div>
  <div class="field" style="left:172px;top:106px;width:156px;height:101px">Comments/Questions</div>
  <div class="send">CONTACT US</div>
</aside>

<div class="tab" style="left:27px;top:829px">OUR SERVICES</div>
<ul class="list services" style="left:27px;top:886px">
  <li>HOME FORTIFICATION</li><li>BAT CONTROL</li><li>OPOSSUM CONTROL</li><li>RACCOON CONTROL</li><li>RAT CONTROL</li><li>OTTER CONTROL</li><li>STARLING CONTROL</li><li>SQUIRREL CONTROL</li>
</ul>

<div class="tab" style="left:379px;top:829px">WHY CHOOSE US?</div>
<ul class="list reasons" style="left:379px;top:886px">
  <li>PNU WILDLIFE BIOLOGIST</li><li>CERTIFIED WILDLIFE PROFESSIONALS</li><li>WA STATE CERTIFIED TRAPPERS</li><li>CERTIFIED MARKSMEN</li><li>BONDED, LICENSED, AND INSURED CONTRACTORS</li><li>HUMANE CERTIFIED PROFESSIONAL ANIMAL CONTROL EXPERT</li><li>WA STATE CERTIFIED NUISANCE WILDLIFE CONTROL OPERATORS</li>
</ul>

<aside class="social">
  FIND US ON<br>FRIENDBOOK
  <div class="social-mark">Tom Varlow</div>
  <div class="like">Like</div>
</aside>

<footer class="foot">
  <nav class="foot-links"><span>HOME</span><span>ABOUT US</span><span>ANIMAL CONTROL</span><span>WILDLIFE SERVICES</span><span>TESTIMONIALS</span><span>CONTACT US</span></nav>
  <div class="pay-label">WE ACCEPT THE FOLLOWING PAYMENT METHODS:</div>
  <div class="pay"><span></span><span>CASH</span><span></span><span></span><span></span><span>CHECK</span><span></span></div>
  <div class="legal">A NORTHWIND ANIMAL CONTROL OF PUGET SOUND | SEATTLE,WA ALL RIGHTS RESERVED | 360-555-0148 | SITEMAP | PRIVACY POLICY</div>
</footer>
</body>
</html>
```